Tavrix - Staffing APP for the hospitality industry.

I need 7 screens designed that form the core of the APP. Tavrix is a staffing APP for the hospitality industry where workers sign up and complete details about themselves and their qualifications and experience. They also switch a button ON and OFF showing their availability status. Venues/employers then scan for workers based on job type, availability, distance etc

Industry/Entity Type

Hospitality employment industry

Number of Pages Required

5+ page

Requirements
Must have
• Refer wire frames supplied
Nice to have
• Here is my website as a guide www.tavrix.com.au
Should not have
• Nil

```html
<!DOCTYPE html>
<html lang="en">
<head>
<meta charset="utf-8">
<title>Tavrix – App Screens</title>
<link href="https://fonts.googleapis.com/css2?family=Urbanist:wght@400;500;600;700;800&display=swap" rel="stylesheet">
<style>
:root{
  --bg:#d9dfe8;
  --screen:#f3f5f9;
  --field:#ffffff;
  --ink:#1f1f24;
  --title:#23233a;
  --muted:#8b909a;
  --soft:#b5bac3;
  --line:#e4e7ec;
  --badge:#7b8089;
  --green:#7ccf8e;
  --photo-a:#3b3f45;
  --photo-b:#8a7a6a;
}
*{box-sizing:border-box;margin:0;padding:0}
html,body{width:1002px;height:1200px;overflow:hidden;background:var(--bg)}
body{font-family:"Urbanist",sans-serif;color:var(--ink);position:relative}
.abs{position:absolute}
.section-label{position:absolute;font-size:12.5px;font-weight:600;color:#5d6470;text-align:center;width:203px;letter-spacing:.2px}
.intro{position:absolute;left:26px;top:152px;width:200px;text-align:center;font-size:9.4px;line-height:20px;color:#4a4f58}
.intro .regards{margin-top:22px}
.screen{position:absolute;width:203px;background:var(--screen);border-radius:17px;overflow:hidden;box-shadow:0 8px 24px rgba(120,130,150,.12)}
.status{position:absolute;top:6px;left:12px;right:9px;display:flex;justify-content:space-between;align-items:center;font-size:8px;font-weight:600;color:var(--ink)}
.status svg{height:6px}
.header{position:absolute;top:32px;left:10px;right:10px;height:23px;display:flex;align-items:center;justify-content:space-between}
.icon-btn{width:23px;height:23px;border-radius:6px;background:var(--field);display:flex;align-items:center;justify-content:center}
.icon-btn svg{width:10px;height:10px}
.header h2{font-size:9.5px;font-weight:700;color:var(--title)}
.label{position:absolute;left:10px;font-size:6.8px;font-weight:600;color:var(--muted)}
.field{position:absolute;left:10px;width:183px;height:25px;background:var(--field);border-radius:4px;font-size:8.3px;display:flex;align-items:center;padding-left:9px;color:var(--ink)}
.field.ph{font-size:6.5px;font-style:italic;color:var(--soft);padding-left:8px}
.caret{display:inline-block;width:1px;height:10px;background:var(--ink);margin-left:2px}
.btn-dark{position:absolute;background:var(--ink);color:#fff;border-radius:4px;display:flex;align-items:center;justify-content:center;font-weight:700;font-size:9px}
.btn-dark svg{position:absolute;left:12px;width:11px;height:11px}
.toggle{position:absolute;width:28px;height:16px;border-radius:8px;background:#eceef2}
.toggle::after{content:"";position:absolute;top:2px;left:2px;width:12px;height:12px;border-radius:50%;background:#fff;box-shadow:0 1px 3px rgba(0,0,0,.18)}
.toggle.on{background:var(--green)}
.toggle.on::after{left:auto;right:2px}
.select svg{position:absolute;right:8px;width:8px;height:8px}
.photo{position:absolute;background:linear-gradient(135deg,var(--photo-a),#5a5752 45%,var(--photo-b));}
.badge{position:absolute;left:71px;width:63px;height:15px;border-radius:4px;background:var(--badge);color:#fff;font-size:7px;font-weight:700;display:flex;align-items:center;justify-content:center}
.seen{position:absolute;width:100%;text-align:center;font-size:7px;color:var(--muted)}
.name{position:absolute;width:100%;text-align:center;font-size:10.5px;font-weight:700}
.pill{position:absolute;left:63px;width:76px;height:19px;background:var(--field);border-radius:4px;display:flex;align-items:center;justify-content:center;gap:8px;font-size:8px;font-weight:700}
.pill small{font-size:6.5px;font-weight:500;color:var(--soft)}
.pill i{width:1px;height:10px;background:var(--line)}
.stat{position:absolute;font-size:7px}
.stat.k{color:var(--muted)}
.stat.v{font-weight:700}
.chip{position:absolute;width:83px;height:22px;background:var(--field);border-radius:4px;font-size:7px;font-weight:700;display:flex;align-items:center;justify-content:space-between;padding:0 7px}
.chip svg{width:9px;height:9px}
.sq{position:absolute;width:27px;height:27px;border-radius:5px;background:var(--field);display:flex;align-items:center;justify-content:center}
.sq svg{width:11px;height:11px}
.row-label{position:absolute;left:13px;font-size:6.8px;font-weight:600;color:var(--muted)}
.yn{position:absolute;left:147px;width:47px;height:22px;background:var(--field);border-radius:4px;display:flex;align-items:center;justify-content:space-around;font-size:7.5px;font-weight:700}
.yn span:last-child{color:var(--soft)}
.yn i{width:1px;height:9px;background:var(--line)}
.area{position:absolute;left:11px;width:183px;height:62px;background:var(--field);border-radius:4px}
.area span{position:absolute;right:5px;bottom:4px;font-size:5.2px;font-style:italic;color:var(--soft)}
</style>
</head>
<body>

<svg width="0" height="0" style="position:absolute">
  <defs>
    <symbol id="i-back" viewBox="0 0 24 24"><path d="M15 5l-7 7 7 7" fill="none" stroke="#1f1f24" stroke-width="2.4" stroke-linecap="round" stroke-linejoin="round"/></symbol>
    <symbol id="i-close" viewBox="0 0 24 24"><path d="M6 6l12 12M18 6L6 18" fill="none" stroke="#1f1f24" stroke-width="2.6" stroke-linecap="round"/></symbol>
    <symbol id="i-down" viewBox="0 0 24 24"><path d="M5 9l7 7 7-7" fill="none" stroke="#1f1f24" stroke-width="2.4" stroke-linecap="round" stroke-linejoin="round"/></symbol>
    <symbol id="i-go" viewBox="0 0 24 24"><rect x="3" y="3" width="18" height="18" rx="5" fill="none" stroke="#1f1f24" stroke-width="1.8"/><path d="M10 8l4 4-4 4" fill="none" stroke="#1f1f24" stroke-width="1.8" stroke-linecap="round"/></symbol>
    <symbol id="i-phone" viewBox="0 0 24 24"><path d="M5 4h4l2 5-2.5 1.5a11 11 0 0 0 5 5L15 13l5 2v4a2 2 0 0 1-2 2A16 16 0 0 1 3 6a2 2 0 0 1 2-2z" fill="none" stroke="currentColor" stroke-width="1.8" stroke-linejoin="round"/></symbol>
    <symbol id="i-heart" viewBox="0 0 24 24"><path d="M12 20s-8-4.6-8-10.2A4.4 4.4 0 0 1 12 7a4.4 4.4 0 0 1 8 2.8C20 15.4 12 20 12 20z" fill="none" stroke="currentColor" stroke-width="1.9" stroke-linejoin="round"/></symbol>
    <symbol id="i-card" viewBox="0 0 24 24"><rect x="4" y="4" width="16" height="16" rx="4" fill="none" stroke="#1f1f24" stroke-width="2"/><path d="M12 4v16M14 9l2 3-2 3" fill="none" stroke="#1f1f24" stroke-width="1.8" stroke-linecap="round"/></symbol>
    <symbol id="i-trash" viewBox="0 0 24 24"><path d="M4 7h16M9 7V4h6v3M6 7l1 13h10l1-13M10 11v5M14 11v5" fill="none" stroke="#1f1f24" stroke-width="1.9" stroke-linecap="round" stroke-linejoin="round"/></symbol>
    <symbol id="i-user" viewBox="0 0 24 24"><circle cx="11" cy="8" r="4" fill="none" stroke="currentColor" stroke-width="1.9"/><path d="M4 20a7 7 0 0 1 12-4.5M17 16v5M14.5 18.5h5" fill="none" stroke="currentColor" stroke-width="1.9" stroke-linecap="round"/></symbol>
    <symbol id="i-home" viewBox="0 0 24 24"><path d="M4 11l8-7 8 7v9H4z" fill="none" stroke="#1f1f24" stroke-width="2" stroke-linejoin="round"/></symbol>
    <symbol id="i-edit" viewBox="0 0 24 24"><path d="M20 13v5a2 2 0 0 1-2 2H6a2 2 0 0 1-2-2V6a2 2 0 0 1 2-2h5M17 4l3 3-8 8H9v-3z" fill="none" stroke="#1f1f24" stroke-width="2" stroke-linejoin="round"/></symbol>
    <symbol id="i-cal" viewBox="0 0 24 24"><rect x="3" y="5" width="18" height="16" rx="3" fill="none" stroke="#1f1f24" stroke-width="2"/><path d="M3 10h18M8 3v4M16 3v4" stroke="#1f1f24" stroke-width="2" stroke-linecap="round"/><path d="M8 14h2M12 14h2M16 14h1M8 17h2M12 17h2" stroke="#1f1f24" stroke-width="1.6"/></symbol>
    <symbol id="i-bars" viewBox="0 0 60 12"><rect x="0" y="8" width="3" height="4" rx="1"/><rect x="5" y="6" width="3" height="6" rx="1"/><rect x="10" y="3" width="3" height="9" rx="1"/><rect x="15" y="0" width="3" height="12" rx="1"/><path d="M25 5a9 9 0 0 1 12 0l-1.6 1.6a6.7 6.7 0 0 0-8.8 0zM28 8a5 5 0 0 1 6 0l-3 3z"/><rect x="42" y="2" width="15" height="8" rx="2"/><rect x="58" y="4.5" width="1.5" height="3"/></symbol>
  </defs>
</svg>

<!-- Intro note -->
<p class="intro">Tell me more about your business and any obstacle on it. We provide all of our clients with personalized web solutions providing them with 100% satisfaction.<br><span class="regards">Best Regards,</span></p>

<!-- Section labels -->
<div class="section-label" style="left:277px;top:51px">Front Page</div>
<div class="section-label" style="left:522px;top:51px">Employer Home</div>
<div class="section-label" style="left:768px;top:51px">Worker Registration</div>
<div class="section-label" style="left:31px;top:383px">Scan Results</div>
<div class="section-label" style="left:278px;top:596px">Scan Worker</div>
<div class="section-label" style="left:524px;top:596px">Favourites</div>

<!-- Front page -->
<section class="screen front" style="left:277px;top:94px;height:441px">
  <div class="photo" role="img" aria-label="Hospitality staff member in a grey suit with hands folded" style="left:0;top:0;width:203px;height:275px;background:linear-gradient(160deg,#6b6b6e,#3e3f43 55%,#55565a)"></div>
  <div class="abs" style="left:0;top:150px;width:203px;text-align:center;color:#fff;font-size:14px;font-weight:600;letter-spacing:2.5px">TAVRIX</div>
  <svg class="abs" style="left:0;top:250px" width="203" height="30" viewBox="0 0 203 30"><path d="M0 12 C40 2 150 -2 203 10 V30 H0z" fill="#fff"/></svg>
  <div class="abs" style="left:0;top:268px;width:203px;height:173px;background:#fff"></div>
  <h1 class="abs" style="left:0;top:287px;width:203px;text-align:center;font-size:14.5px;font-weight:800;line-height:18px">Australia's Hospitality<br>Staff Pool.</h1>
  <p class="abs" style="left:0;top:329px;width:203px;text-align:center;font-size:8px;color:#5d6470">What are you waiting for? Dive in!</p>
  <div class="btn-dark" style="left:13px;top:365px;width:177px;height:27px">Get Started</div>
  <p class="abs" style="left:0;top:408px;width:203px;text-align:center;font-size:7.8px;color:#4a4f58">Already have an account?&nbsp; <b style="color:var(--ink)">Sign In</b></p>
</section>

<!-- Employer home -->
<section class="screen employer" style="left:522px;top:94px;height:441px">
  <div class="status"><span>9:41</span><svg viewBox="0 0 60 12" width="34"><use href="#i-bars"/></svg></div>
  <div class="header">
    <div class="icon-btn"><svg><use href="#i-home"/></svg></div>
    <h2>Employer</h2>
    <div class="icon-btn"><svg><use href="#i-edit"/></svg></div>
  </div>
  <span class="label" style="top:70px">Venue Name</span>
  <div class="field" style="top:84px">Wonderland<span class="caret"></span></div>
  <span class="label" style="top:120px">Contact Person</span>
  <div class="field" style="top:134px">Alice</div>
  <span class="label" style="top:170px">Email Address</span>
  <div class="field" style="top:184px">alice.venue@mailhub.com</div>
  <span class="label" style="top:220px">Phone Number</span>
  <div class="field" style="top:234px">alice.venue@mailhub.com</div>
  <span class="label" style="top:270px">Location</span>
  <div class="field" style="top:284px;height:52px;align-items:flex-start;padding-top:8px">Alice</div>
  <div class="btn-dark" style="left:10px;top:352px;width:130px;height:27px;color:#fff"><svg style="color:#fff"><use href="#i-user"/></svg>Scan Worker</div>
  <div class="btn-dark" style="left:10px;top:385px;width:130px;height:27px;color:#fff"><svg style="color:#fff"><use href="#i-heart"/></svg>Scan Favourite</div>
  <div class="btn-dark" style="left:146px;top:352px;width:47px;height:60px;flex-direction:column;line-height:16px;font-size:8.3px">Legal<span style="font-size:12px;font-weight:400">+</span>Payments</div>
</section>

<!-- Worker registration -->
<section class="screen register" style="left:768px;top:94px;height:835px">
  <div class="status"><span>9:41</span><svg viewBox="0 0 60 12" width="34"><use href="#i-bars"/></svg></div>
  <div class="header">
    <div class="icon-btn"><svg><use href="#i-back"/></svg></div>
    <h2>Worker Registration</h2>
    <div class="icon-btn"><svg><use href="#i-close"/></svg></div>
  </div>
  <div class="photo" role="img" aria-label="Profile photo of a chef plating a dish" style="left:62px;top:62px;width:78px;height:93px;border-radius:9px"></div>
  <span class="label" style="top:171px">First Name</span>
  <div class="field" style="top:187px">Harman<span class="caret"></span></div>
  <span class="label" style="top:221px">Email Address</span>
  <div class="field" style="top:236px"></div>
  <span class="label" style="top:271px">Mobile Phone</span>
  <div class="field" style="top:286px"></div>
  <span class="label" style="top:321px">Location</span>
  <div class="field ph" style="top:336px;width:66px">Street Number</div>
  <div class="field ph" style="top:336px;left:82px;width:111px">Street Name</div>
  <div class="field ph" style="top:365px">Suburb / City</div>
  <div class="field ph" style="top:395px;width:111px">State</div>
  <div class="field ph" style="top:395px;left:127px;width:66px">Post Code</div>
  <span class="row-label" style="top:436px">D.O.B</span>
  <div class="field" style="top:428px;left:46px;width:147px;height:21px"><svg class="abs" style="right:7px;width:10px;height:10px"><use href="#i-cal"/></svg></div>
  <span class="row-label" style="top:465px">RSA</span>
  <div class="toggle" style="left:62px;top:462px"></div>
  <span class="row-label" style="top:465px;left:116px">SFA</span>
  <div class="toggle on" style="left:163px;top:462px"></div>
  <span class="row-label" style="top:492px">Vaccination Status</span>
  <div class="field select" style="top:485px;left:93px;width:100px;height:20px"><svg><use href="#i-down"/></svg></div>
  <span class="row-label" style="top:522px">Eligible to work in Australia</span>
  <div class="yn" style="top:515px"><span>Y</span><i></i><span>N</span></div>
  <span class="row-label" style="top:552px">ABN</span>
  <div class="yn" style="top:545px"><span>Y</span><i></i><span>N</span></div>
  <span class="row-label" style="top:576px">Qualification</span>
  <div class="area" style="top:591px"><span>500 Words</span></div>
  <span class="abs" style="left:89px;top:648px;font-size:11.5px;font-weight:500;color:#4a4f58">Cart</span>
  <span class="row-label" style="top:668px">Experience</span>
  <div class="area" style="top:682px"><span>500 Words</span></div>
  <span class="row-label" style="top:761px">Select Categories</span>
  <div class="field select" style="top:755px;left:93px;width:100px;height:20px"><svg><use href="#i-down"/></svg></div>
  <div class="btn-dark" style="left:11px;top:790px;width:148px;height:27px">Save Information</div>
  <div class="sq" style="left:167px;top:790px;width:25px"><svg><use href="#i-trash"/></svg></div>
</section>

<!-- Scan results -->
<section class="screen results" style="left:31px;top:427px;height:440px">
  <div class="status"><span>9:41</span><svg viewBox="0 0 60 12" width="34"><use href="#i-bars"/></svg></div>
  <div class="header">
    <div class="icon-btn"><svg><use href="#i-back"/></svg></div>
    <h2>Scan Results</h2>
    <div class="icon-btn"><svg><use href="#i-close"/></svg></div>
  </div>
  <div class="badge" style="top:62px">Chef</div>
  <div class="seen" style="top:83px">Last seen 2hr ago</div>
  <div class="photo" role="img" aria-label="Neighbouring worker card" style="left:11px;top:113px;width:169px;height:135px;border-radius:8px;opacity:.35"></div>
  <div class="photo" role="img" aria-label="Chef plating a dish in a kitchen" style="left:34px;top:98px;width:136px;height:156px;border-radius:9px"></div>
  <div class="name" style="top:264px">Peter</div>
  <div class="pill" style="top:279px">28 <small>yr</small><i></i>15 <small>km</small></div>
  <span class="stat k" style="left:15px;top:310px">RSA</span><span class="stat v" style="left:74px;top:310px">Yes</span>
  <span class="stat k" style="left:115px;top:310px">SFH</span><span class="stat v" style="left:174px;top:310px">Yes</span>
  <span class="stat k" style="left:15px;top:325px">Vax Status</span><span class="stat v" style="left:78px;top:325px">F</span>
  <span class="stat k" style="left:115px;top:325px">ABN</span><span class="stat v" style="left:175px;top:325px">No</span>
  <div class="chip" style="left:13px;top:344px">Qualification<svg><use href="#i-go"/></svg></div>
  <div class="chip" style="left:106px;top:344px">Experience<svg><use href="#i-go"/></svg></div>
  <div class="btn-dark" style="left:13px;top:384px;width:109px;height:27px"><svg style="color:#fff"><use href="#i-phone"/></svg>Reveal</div>
  <div class="sq" style="left:128px;top:384px;color:var(--ink)"><svg><use href="#i-heart"/></svg></div>
  <div class="sq" style="left:164px;top:384px"><svg><use href="#i-card"/></svg></div>
</section>

<!-- Scan worker -->
<section class="screen scan" style="left:278px;top:646px;height:440px">
  <div class="status"><span>9:41</span><svg viewBox="0 0 60 12" width="34"><use href="#i-bars"/></svg></div>
  <div class="header">
    <div class="icon-btn"><svg><use href="#i-back"/></svg></div>
    <h2>Scan Worker</h2>
    <div class="icon-btn"><svg><use href="#i-close"/></svg></div>
  </div>
  <span class="label" style="left:16px;top:70px">Job Type</span>
  <div class="field select" style="top:85px;left:11px;width:182px;height:24px">Choices<svg><use href="#i-down"/></svg></div>
  <span class="label" style="left:17px;top:127px">Available now</span>
  <div class="toggle" style="left:165px;top:124px"></div>
  <span class="label" style="left:17px;top:159px">Distances</span>
  <div class="field" style="top:152px;left:141px;width:52px;height:23px;padding-left:15px;font-weight:700;font-size:8px">15 <small style="font-weight:400;color:var(--soft);margin-left:10px;font-size:7px">km</small></div>
  <span class="label" style="left:17px;top:187px">Sort by</span>
  <div class="field select" style="top:201px;left:11px;width:182px;color:#6b707a">Choices<svg><use href="#i-down"/></svg></div>
  <div class="btn-dark" style="left:13px;top:245px;width:177px;height:27px">Start Scan</div>
</section>

<!-- Favourites -->
<section class="screen favourites" style="left:524px;top:646px;height:440px">
  <div class="status"><span>9:41</span><svg viewBox="0 0 60 12" width="34"><use href="#i-bars"/></svg></div>
  <div class="header">
    <div class="icon-btn"><svg><use href="#i-back"/></svg></div>
    <h2>Favourites</h2>
    <div class="icon-btn"><svg><use href="#i-close"/></svg></div>
  </div>
  <div class="badge" style="top:63px">Chef</div>
  <div class="seen" style="top:84px">Last seen 2hr ago</div>
  <div class="photo" role="img" aria-label="Neighbouring worker card" style="left:11px;top:114px;width:169px;height:135px;border-radius:8px;opacity:.35"></div>
  <div class="photo" role="img" aria-label="Chef plating a dish in a kitchen" style="left:34px;top:99px;width:136px;height:156px;border-radius:9px"></div>
  <div class="name" style="top:265px">Peter</div>
  <div class="pill" style="top:280px">28 <small>yr</small><i></i>15 <small>km</small></div>
  <span class="stat k" style="left:15px;top:311px">RSA</span><span class="stat v" style="left:74px;top:311px">Yes</span>
  <span class="stat k" style="left:115px;top:311px">SFH</span><span class="stat v" style="left:174px;top:311px">Yes</span>
  <span class="stat k" style="left:15px;top:326px">Vax Status</span><span class="stat v" style="left:78px;top:326px">F</span>
  <span class="stat k" style="left:115px;top:326px">ABN</span><span class="stat v" style="left:175px;top:326px">No</span>
  <div class="chip" style="left:13px;top:345px">Qualification<svg><use href="#i-go"/></svg></div>
  <div class="chip" style="left:106px;top:345px">Experience<svg><use href="#i-go"/></svg></div>
  <div class="btn-dark" style="left:13px;top:385px;width:109px;height:27px"><svg style="color:#fff"><use href="#i-phone"/></svg>Reveal</div>
  <div class="sq" style="left:128px;top:385px"><svg><use href="#i-trash"/></svg></div>
  <div class="sq" style="left:164px;top:385px"><svg><use href="#i-card"/></svg></div>
</section>

</body>
</html>
```